A professional business to business web site for a contract agency called VANTOMER.

We need a very clean, very professional web site created for business to business. It is an informational web site with 3 pages. We are a company that offers contract employee placements into primarily the pharmaceutical industry. I have attached a file that describes the company more fully.
Updates

Hi,

I'm sorry if I wasn't clear, but I need to have the HTML pages created so I can just upload the files you give me to the web hosting site.

Please let me know if you have any questions.

Thanks for working on my project!

Hello,

I didn't put this in the description, but I would need the web site set up on the web hosting site as well.  The web hosting site is bluepinecrest.  I want a copy of all the files as well.

Thanks,
Milo

Reason: I'm sorry, unexpectedly, I have been very busy and I haven't been able to devote the time necessary for this. I am extending the deadline by 10 days. Thank you for your patience. Thanks.

Reason: Hi everyone, I apologize again, but everything has been so busy here that I haven't been able to give this attention. I plan to work on this over the next few days. Thanks and sorry again, Milo.

Reason: I'm sorry this is taking longer than planned. I have been extremely busy. I have increased the budget on this project. Thanks.

Target Market(s)

Large professional corporations mainly in the pharmaceutical industry. The audience is hiring decisions makers within the companies and potential job candidates/job seekers.

Industry/Entity Type

Pharmaceutical

Font styles to use
Sans Serif

Requirements
Must have
• Must have a clean look that mimics the pharmaceutical industry web sites. VERY professional.
Nice to have
• A nice picture of professional business/pharma/technical people looking like a team. Colors are listed on the attached Word document.
Should not have
• No animation. Not too busy.

```html
<!DOCTYPE html>
<html lang="en">
<head>
<meta charset="utf-8">
<title>Vantomer</title>
<link href="https://fonts.googleapis.com/css2?family=Hind:wght@400;500&display=swap" rel="stylesheet">
<style>
:root{
  --navy:#0c4393;
  --navy-dark:#093a80;
  --text:#2a2a2a;
  --muted:#6b6b6b;
  --rule:#dcdcdc;
  --white:#fff;
}
*{margin:0;padding:0;box-sizing:border-box}
html,body{width:831px;height:1200px;overflow:hidden;background:var(--white)}
body{font-family:'Hind',sans-serif;color:var(--text);position:relative}
.header{height:69px;position:relative}
.brand{position:absolute;left:92px;top:28px;display:flex;align-items:center;gap:8px;color:var(--navy);font-size:17px;letter-spacing:3px;font-weight:500}
.brand-dot{width:12px;height:12px;border-radius:50%;background:var(--navy)}
.search{position:absolute;left:578px;top:23px;width:163px;height:26px;border:1px solid #d5d5d5;border-radius:2px}
.search-btn{position:absolute;right:0;top:0;width:28px;height:24px;border-left:1px solid #d5d5d5;display:flex;align-items:center;justify-content:center}
.nav{height:36px;background:var(--navy);border-bottom:4px solid #6f95cf;display:flex;padding-left:99px}
.nav a{color:var(--white);font-size:10px;text-decoration:none;line-height:34px;margin-right:38px}
.hero{height:311px;position:relative;
  background:
    radial-gradient(ellipse 90px 70px at 62% 85%,rgba(40,170,210,.75),transparent),
    radial-gradient(ellipse 80px 90px at 78% 42%,rgba(60,160,200,.6),transparent),
    radial-gradient(ellipse 220px 260px at 74% 40%,rgba(240,242,246,.95),transparent 70%),
    linear-gradient(90deg,#2c6bbd 0%,#4f86cc 30%,#8fb4df 50%,#dfe8f2 68%,#eef2f7 85%,#cfdceb 100%)}
.hero-caption{position:absolute;left:90px;top:111px;width:272px;height:98px;background:rgba(20,40,70,.72);padding:14px 17px;color:var(--white);font-size:10.5px;line-height:18px}
.dots{display:flex;gap:3px;margin-top:7px}
.dots span{width:9px;height:9px;border-radius:50%;background:var(--navy)}
.dots span:first-child{background:#8fb5e6}
.features{display:flex;justify-content:space-between;padding:47px 109px 0 108px;height:217px}
.feature{width:170px;text-align:center}
.feature-icon{width:65px;height:65px;border:3px solid var(--navy);border-radius:50%;margin:0 auto 12px;display:flex;align-items:center;justify-content:center}
.feature h3{font-weight:400;font-size:14px;margin-bottom:6px}
.feature p{font-size:9.3px;color:var(--muted);line-height:14px}
.service p,.welcome p{font-size:9px;color:var(--muted);line-height:14px}
.more{color:var(--navy);font-style:italic;margin-left:3px}
.rule{height:1px;background:var(--rule);margin:0 90px}
.welcome{display:flex;padding:36px 90px 0;height:193px;gap:18px}
.welcome-text{width:430px}
h2{font-weight:400;font-size:17px;margin-bottom:14px}
h2 em{font-style:normal;color:var(--navy)}
.welcome p{line-height:15.5px;margin-bottom:16px}
.video{width:208px;height:121px;background:linear-gradient(135deg,#2c4a78,#9fb4cf 60%,#e8d8cc);display:flex;align-items:center;justify-content:center}
.services{padding:25px 90px 0}
.services h2{margin-bottom:8px}
.service-grid{display:flex;gap:13px}
.service{width:208px}
.photo{height:121px;margin-bottom:19px}
.service h3{font-weight:400;font-size:12px;margin-bottom:8px}
.service p{line-height:15.5px}
.footer{position:absolute;left:0;top:1137px;width:831px;height:63px;background:var(--navy);color:var(--white);font-size:9px}
.footer small{position:absolute;left:92px;top:26px;font-size:9px}
.social{position:absolute;right:90px;top:22px;display:flex;gap:5px}
.social span{width:19px;height:19px;border-radius:50%;background:#e9e9e9}
</style>
</head>
<body>
<header class="header">
  <div class="brand"><span class="brand-dot"></span>VANTOMER</div>
  <div class="search"><div class="search-btn"><svg width="9" height="9" viewBox="0 0 10 10"><circle cx="4" cy="4" r="3" fill="none" stroke="#333" stroke-width="1.5"/><line x1="6.2" y1="6.2" x2="9" y2="9" stroke="#333" stroke-width="1.6"/></svg></div></div>
</header>
<nav class="nav"><a>Home</a><a>About us</a><a>Services</a><a>Gallery</a><a>Blog</a><a>Testimonials</a><a>Contact us</a></nav>
<section class="hero" role="img" aria-label="Scientist in goggles and blue gloves working with a pipette in a laboratory">
  <div class="hero-caption">We provide contract employee placement to pharma-ceutical industry. So we are manpower consultancy for Pharma industry alone.
    <div class="dots"><span></span><span></span><span></span><span></span></div></div>
</section>
<section class="features">
  <div class="feature"><div class="feature-icon"><svg width="22" height="20" viewBox="0 0 22 20"><rect x="1" y="4" width="20" height="15" rx="2" fill="#0c4393"/><rect x="7" y="1" width="8" height="4" rx="1" fill="none" stroke="#0c4393" stroke-width="2"/><path d="M11 8v8M7 12h8" stroke="#fff" stroke-width="2.4"/></svg></div>
    <h3>Pharma Carreer</h3><p>Neque porro quisquam est qui dolorem ipsum quia dolor sit amet consectetur adipisci velit.<span class="more">Read More &gt;&gt;</span></p></div>
  <div class="feature"><div class="feature-icon"><svg width="32" height="28" viewBox="0 0 32 28"><circle cx="12" cy="11" r="6.5" fill="#0c4393"/><circle cx="12" cy="11" r="8" fill="none" stroke="#0c4393" stroke-width="3.2" stroke-dasharray="3.1 3.2"/><circle cx="12" cy="11" r="2.6" fill="#fff"/><circle cx="24.5" cy="20.5" r="3.6" fill="#0c4393"/><circle cx="24.5" cy="20.5" r="4.6" fill="none" stroke="#0c4393" stroke-width="2" stroke-dasharray="1.8 1.8"/><circle cx="24.5" cy="20.5" r="1.4" fill="#fff"/></svg></div>
    <h3>Custom Control</h3><p>Neque porro quisquam est qui dolorem ipsum quia dolor sit amet consectetur adipisci velit.<span class="more">Read More &gt;&gt;</span></p></div>
  <div class="feature"><div class="feature-icon"><svg width="24" height="20" viewBox="0 0 24 20"><circle cx="9" cy="5" r="4" fill="#0c4393"/><path d="M1 19c0-6 3-8 8-8s8 2 8 8z" fill="#0c4393"/><circle cx="17" cy="9" r="3" fill="#0c4393"/><path d="M13 19c0-4 2-6 5-6s5 2 5 6z" fill="#0c4393"/></svg></div>
    <h3>Membership</h3><p>Neque porro quisquam est qui dolorem ipsum quia dolor sit amet consectetur adipisci velit.<span class="more">Read More &gt;&gt;</span></p></div>
</section>
<div class="rule"></div>
<section class="welcome">
  <div class="welcome-text"><h2>Welcome to Our Website <em>Mainpage...</em></h2>
    <p>Lorem ipsum dolor sit amet, consectetur adipisicing elit, sed do eiusmos tempor incididunt ut labore et dolore magna aliqua. Ut enim ad minimu quis nostrud exercitation ullamco laboris nisi ut aliquip ex ea commodse consequat. Duis aute irure dolor in reprehenderit</p>
    <p>Voluptate velit esse cillum dolore eu fugiat nulla pariatur. Excepteur sint occaecat cupidatat non proi-dent, sunt in culpa qui officia deserunt mollit anim id est laborum</p></div>
  <div class="video" role="img" aria-label="Video still of two scientists examining a sample"><svg width="52" height="52" viewBox="0 0 52 52"><circle cx="26" cy="26" r="25" fill="rgba(40,40,40,.7)"/><path d="M20 14l16 12-16 12z" fill="#fff"/></svg></div>
</section>
<div class="rule"></div>
<section class="services"><h2>Our <em>Services</em></h2>
  <div class="service-grid">
    <div class="service"><div class="photo" role="img" aria-label="Lab team working at microscopes" style="background:linear-gradient(135deg,#5a7fa8,#d9e2ec)"></div><h3>Project Management</h3><p>Voluptate velit esse cillum dolore eu fugiat nulla pariatur. Excepteur sint occaecat cupidatat non proident, sunt in culpa qui.</p></div>
    <div class="service"><div class="photo" role="img" aria-label="Pill bottles with scattered tablets and capsules" style="background:linear-gradient(135deg,#e58a2a,#f1e6e4 55%,#d7849a)"></div><h3>Software Traning</h3><p>Voluptate velit esse cillum dolore eu fugiat nulla pariatur. Excepteur sint occaecat cupidatat non proident, sunt in culpa qui.</p></div>
    <div class="service"><div class="photo" role="img" aria-label="Researcher looking into a microscope" style="background:linear-gradient(135deg,#d6d9dd,#8aa2b8)"></div><h3>Laboratory Position</h3><p>Voluptate velit esse cillum dolore eu fugiat nulla pariatur. Excepteur sint occaecat cupidatat non proident, sunt in culpa qui.</p></div>
  </div>
</section>
<footer class="footer"><small>©2014. Vantomer. All Right Reserved.</small>
  <div class="social"><span></span><span></span><span></span><span></span></div></footer>
</body>
</html>
```